Microlight Aircraft Website Project

Need a website designed, or at least a template made, that my web programmer can work with here. We are a new manufacturer of microlight aircraft & powered hang gliders. Our company name is Brisk Fern. We manufacture portable utility aircraft in the Light Sport category (formerly known as Ultralights or Microlights). Our particular design is a 2-seat powered hang glider and caters to those who want to go explore the backcountry. We are not necessarily aviation nuts, but more into the development of a flying utility vehicle for extreme exploration and expeditions. We have been importing these aircraft from 3 countries for 15 years and have supplied over 200 expedition-quality aircraft world-wide. We are now manufacturing here in the US.

Industry/Entity Type

Manufacturer

Coding

Coded - Design and coding required

```html
<!DOCTYPE html>
<html lang="en">
<head>
<meta charset="utf-8">
<title>Brisk Fern — Microlight Aircraft</title>
<link href="https://fonts.googleapis.com/css2?family=Open+Sans:wght@400;600;700;800&display=swap" rel="stylesheet">
<style>
:root{
  --navy:#0b1150;
  --navy-deep:#080d3c;
  --royal:#1a2aa8;
  --sky:#3d6fd0;
  --ink:#2b2b2b;
  --text:#555a66;
  --paper:#ffffff;
  --mist:#eef0f2;
  --charcoal:#1f1f21;
  --slate:#3a3d42;
}
*{margin:0;padding:0;box-sizing:border-box}
html,body{width:1200px;height:3614px;overflow:hidden}
body{position:relative;background:var(--paper);font-family:'Open Sans',Arial,sans-serif;color:var(--ink)}
.section{position:absolute;left:0;width:1200px;overflow:hidden}

/* hero */
.hero{top:0;height:683px;background:linear-gradient(180deg,#6f9fd6 0%,#3f79c8 35%,#1e4fae 60%,#2a5a8a 80%,#8a7a58 100%)}
.hero-photo{position:absolute;inset:0;background:
  radial-gradient(ellipse 260px 200px at 680px 430px,rgba(225,210,60,.55),transparent 70%),
  radial-gradient(ellipse 500px 260px at 1050px 520px,rgba(95,110,70,.6),transparent 70%),
  linear-gradient(180deg,rgba(255,255,255,.0),rgba(0,0,0,.15))}
.brand{position:absolute;left:100px;top:86px;display:flex;align-items:center;gap:10px;color:var(--paper);font-weight:700;font-size:24px;letter-spacing:1px}
.brand-dot{width:16px;height:16px;background:var(--paper);border-radius:50%}
.nav{position:absolute;left:96px;top:145px;width:1001px;height:53px;background:rgba(20,22,30,.82)}
.nav ul{list-style:none;display:flex;height:100%}
.nav li{color:#e6e8ee;font-size:17px;padding:0 19px;line-height:53px;text-transform:uppercase}
.nav li.active{background:var(--royal);color:var(--paper);font-weight:700;padding:0 26px}
.nav-search{position:absolute;right:0;top:0;width:58px;height:53px;background:#555961}
.hero-arrow{position:absolute;top:425px}
.hero-title{position:absolute;left:99px;top:528px;color:var(--paper);font-weight:700;font-size:38px;line-height:47px;text-shadow:0 1px 3px rgba(0,0,0,.3)}
.dots{position:absolute;left:565px;top:638px;display:flex;gap:7px}
.dots span{width:16px;height:16px;border:2px solid var(--paper);border-radius:50%}
.dots span.on{background:var(--paper)}

/* welcome */
.welcome{top:683px;height:602px;text-align:center}
.welcome-kicker{position:absolute;left:0;width:100%;top:160px;font-size:48px;font-weight:600;color:var(--slate);letter-spacing:1px;line-height:60px}
.welcome-name{position:absolute;left:0;width:100%;top:192px;font-size:76px;font-weight:800;color:var(--navy);letter-spacing:4px;line-height:90px}
.welcome-copy{position:absolute;left:101px;width:998px;top:310px;font-size:17.5px;line-height:28px;color:var(--text)}
.btn{position:absolute;background:var(--navy);color:var(--paper);font-size:15px;text-transform:uppercase;text-align:center}
.welcome .btn{left:511px;top:505px;width:178px;height:42px;line-height:42px;border-radius:3px}

/* services */
.services{top:1285px;height:679px;background:linear-gradient(180deg,#3a3c38 0%,#2c2e2a 40%,#4a4836 70%,#2a2b26 100%)}
.services::after{content:"";position:absolute;inset:0;background:rgba(0,0,0,.35)}
.section-title{position:absolute;left:0;width:100%;text-align:center;font-weight:700;font-size:48px;letter-spacing:1px}
.services .section-title{top:60px;color:var(--paper);z-index:2}
.card{position:absolute;top:168px;width:316px;height:417px;z-index:2}
.card-photo{height:207px}
.card-title{height:46px;line-height:46px;background:#1b1b1d;color:var(--paper);text-align:center;font-weight:600;font-size:21px;letter-spacing:1px}
.card-body{height:126px;background:var(--mist);color:var(--text);font-size:17px;line-height:26px;text-align:center;padding:20px 26px}
.card-more{height:38px;line-height:38px;text-align:center;color:#d8d8d8;font-size:15px;background:#151517;clip-path:polygon(0 0,100% 0,95% 100%,5% 100%)}
.card.mid .card-title,.card.mid .card-more{background:var(--navy)}

/* featured */
.featured{top:1964px;height:586px}
.featured .section-title{top:60px;color:var(--navy)}
.product{position:absolute;top:161px;width:320px;text-align:center}
.product-ring{width:320px;height:320px;border-radius:50%;border:5px solid #d9dadc;padding:6px;background:var(--paper)}
.product-photo{width:100%;height:100%;border-radius:50%}
.product-name{margin-top:20px;font-size:22px;color:var(--slate);letter-spacing:1px}
.product.mid .product-name{font-weight:700;color:var(--navy)}

/* blog */
.blog{top:2550px;height:607px;background:linear-gradient(180deg,#e4e6e8,#c9ccd0 60%,#b8bbbf)}
.blog .section-title{top:70px;color:var(--slate)}
.blog-card{position:absolute;left:125px;top:166px;width:456px;height:362px}
.blog-photo{height:241px}
.blog-text{height:121px;background:var(--navy);color:var(--paper);font-size:19px;line-height:28px;padding:34px 24px;text-align:center}
.blog-feature{position:absolute;left:622px;top:166px;width:453px;height:362px}
.blog-arrow{position:absolute;top:330px}

/* newsletter */
.newsletter{top:3157px;height:97px;background:var(--charcoal)}
.newsletter-title{position:absolute;left:139px;top:26px;color:var(--paper);font-size:36px;font-weight:600;letter-spacing:2px}
.newsletter-rule{position:absolute;left:418px;top:22px;width:1px;height:53px;background:#555}
.newsletter-note{position:absolute;left:450px;top:30px;width:230px;color:#cfd0d4;font-size:14px;line-height:18px}
.newsletter-field{position:absolute;left:694px;top:30px;width:268px;height:40px;background:var(--paper);color:#9a9ca2;font-size:14px;line-height:40px;padding-left:12px}
.newsletter .btn{left:962px;top:30px;width:99px;height:40px;line-height:40px;font-size:14px;text-transform:none;font-weight:600}

/* contact */
.contact{top:3254px;height:289px}
.map{position:absolute;inset:0;background:linear-gradient(135deg,#e8e4d6,#d8dcc8 40%,#e6e2d2 70%,#cfd8e0)}
.map-pin{position:absolute;left:535px;top:90px}
.contact-box{position:absolute;left:766px;top:43px;width:275px;height:198px;background:#1d1d1f;color:var(--paper);padding:20px 28px;font-size:14px;line-height:18px;font-style:normal}
.contact-box h4{font-size:14px;font-weight:700;margin-bottom:10px;letter-spacing:.5px}
.contact-row{display:flex;gap:8px;margin-bottom:14px}
.contact-row svg{flex:none;margin-top:2px}

/* footer */
.footer{top:3543px;height:71px;background:var(--navy-deep);color:var(--paper);font-size:14px}
.footer-copy{position:absolute;left:100px;top:26px}
.footer-social{position:absolute;right:100px;top:17px;display:flex;align-items:center;gap:6px}
.footer-social span.label{margin-right:8px}
.footer-social i{display:block;width:35px;height:35px;border-radius:50%;background:var(--paper)}
</style>
</head>
<body>

<header class="section hero">
  <div class="hero-photo" role="img" aria-label="Pilot flying a yellow two-seat powered hang glider over a blue lake and shoreline"></div>
  <div class="brand"><span class="brand-dot"></span>Brisk Fern</div>
  <nav class="nav">
    <ul>
      <li class="active">Home</li><li>About Us</li><li>Services</li><li>Shop</li><li>Blog</li><li>Contact Us</li>
    </ul>
    <div class="nav-search">
      <svg width="58" height="53" viewBox="0 0 58 53"><circle cx="26" cy="23" r="9" fill="none" stroke="#fff" stroke-width="3"/><line x1="32.5" y1="29.5" x2="40" y2="37" stroke="#fff" stroke-width="4" stroke-linecap="round"/></svg>
    </div>
  </nav>
  <svg class="hero-arrow" style="left:46px" width="30" height="32" viewBox="0 0 30 32"><polygon points="26,3 26,29 4,16" fill="none" stroke="#fff" stroke-width="3"/></svg>
  <svg class="hero-arrow" style="left:1124px" width="30" height="32" viewBox="0 0 30 32"><polygon points="4,3 4,29 26,16" fill="none" stroke="#fff" stroke-width="3"/></svg>
  <h1 class="hero-title">Let's enjoy the wonders<br>of the nature together!</h1>
  <div class="dots"><span class="on"></span><span></span><span></span></div>
</header>

<section class="section welcome">
  <div class="welcome-kicker">WELCOME TO</div>
  <h2 class="welcome-name">BRISK FERN</h2>
  <p class="welcome-copy">Lorem Ipsum is simply dummy text of the printing and typesetting industry. Lorem Ipsum has been the industry's standard dummy text ever since the 1500s, when an unknown printer took a galley of type and scrambled it to make a type specimen book. It has survived not only five centuries, but also the leap into electronic typesetting, remaining essentially unchanged. It was popularised in the 1960s with the release of dry-transfer sheets containing Lorem Ipsum passages, and more recently with desktop publishing software like page layout programs including versions of Lorem Ipsum.</p>
  <div class="btn">Read More</div>
</section>

<section class="section services" role="img" aria-label="Dusky airfield with a microlight wing in the background">
  <h2 class="section-title">SERVICES</h2>
  <article class="card" style="left:99px">
    <div class="card-photo" role="img" aria-label="Two people seated in a powered hang glider trike" style="background:linear-gradient(160deg,#c8d2dc,#8a8f8a 60%,#5a5f58)"></div>
    <div class="card-title">LOREM IPSUM</div>
    <div class="card-body">Lorem Ipsum is simply dummy text of the printing and typesetting industry.</div>
    <div class="card-more">READ MORE</div>
  </article>
  <article class="card mid" style="left:443px">
    <div class="card-photo" role="img" aria-label="White microlight aircraft parked on grass" style="background:linear-gradient(180deg,#7fa8d8,#b9cde6 50%,#7d8a60 80%,#5e6a48)"></div>
    <div class="card-title">LOREM IPSUM</div>
    <div class="card-body">Lorem Ipsum is simply dummy text of the printing and typesetting industry.</div>
    <div class="card-more">READ MORE</div>
  </article>
  <article class="card" style="left:786px">
    <div class="card-photo" role="img" aria-label="Powered hang glider in flight over water at sunset" style="background:linear-gradient(170deg,#c8d8e4,#8fa8c0 50%,#d8a890 75%,#6a7a8a)"></div>
    <div class="card-title">LOREM IPSUM</div>
    <div class="card-body">Lorem Ipsum is simply dummy text of the printing and typesetting industry.</div>
    <div class="card-more">READ MORE</div>
  </article>
</section>

<section class="section featured">
  <h2 class="section-title">FEATURED PRODUCTS</h2>
  <div class="product" style="left:98px">
    <div class="product-ring"><div class="product-photo" role="img" aria-label="Pilot and passenger in a hang glider trike over a harbour" style="background:linear-gradient(150deg,#9fb4c8,#7a6e5a 60%,#b0705a)"></div></div>
    <div class="product-name">LOREM IPSUM</div>
  </div>
  <div class="product mid" style="left:443px">
    <div class="product-ring"><div class="product-photo" role="img" aria-label="Blue-toned view of a hang glider trike from above" style="background:linear-gradient(160deg,#aebde8,#2c3d9c 55%,#1a2580)"></div></div>
    <div class="product-name">LOREM IPSUM</div>
  </div>
  <div class="product" style="left:785px">
    <div class="product-ring"><div class="product-photo" role="img" aria-label="Microlight with a blue wing on an airfield" style="background:linear-gradient(180deg,#8cb0e0,#d8e2ee 45%,#7a8a5a 75%,#5a6640)"></div></div>
    <div class="product-name">LOREM IPSUM</div>
  </div>
</section>

<section class="section blog" role="img" aria-label="Faded greyscale hang glider over a valley">
  <h2 class="section-title">BLOG</h2>
  <svg class="blog-arrow" style="left:36px" width="34" height="40" viewBox="0 0 34 40"><polygon points="30,3 30,37 4,20" fill="none" stroke="#3a3d42" stroke-width="3"/></svg>
  <article class="blog-card">
    <div class="blog-photo" role="img" aria-label="Hang glider with a pink wing parked beside a building" style="background:linear-gradient(180deg,#9aa0a8,#8a8c80 50%,#4e5a3a)"></div>
    <p class="blog-text">Lorem Ipsum is simply dummy text of the printing and typesetting industry.</p>
  </article>
  <div class="blog-feature" role="img" aria-label="Two pilots in a green-framed trike flying above clouds" style="background:linear-gradient(170deg,#1e5ec0,#4a8ae0 40%,#b8d4f0 75%,#eaf2fa)"></div>
  <svg class="blog-arrow" style="left:1130px" width="34" height="40" viewBox="0 0 34 40"><polygon points="4,3 4,37 30,20" fill="none" stroke="#0b1150" stroke-width="3"/></svg>
</section>

<section class="section newsletter">
  <h2 class="newsletter-title">NEWSLETTER</h2>
  <div class="newsletter-rule"></div>
  <p class="newsletter-note">Signup to get exciting offers<br>and updates</p>
  <div class="newsletter-field">Enter Your Email Here...</div>
  <div class="btn">Subscribe</div>
</section>

<section class="section contact">
  <div class="map" role="img" aria-label="Street map of the surrounding neighbourhood"></div>
  <svg class="map-pin" width="30" height="42" viewBox="0 0 30 42"><path d="M15 1C7 1 1 7 1 15c0 10 14 26 14 26s14-16 14-26C29 7 23 1 15 1z" fill="#1d1d1f"/><circle cx="15" cy="15" r="5" fill="#fff"/></svg>
  <address class="contact-box">
    <h4>CONTACT US</h4>
    <div class="contact-row">
      <svg width="12" height="15" viewBox="0 0 12 15"><path d="M6 0C3 0 0 2.5 0 6c0 4 6 9 6 9s6-5 6-9c0-3.5-3-6-6-6z" fill="#fff"/><circle cx="6" cy="6" r="2" fill="#1d1d1f"/></svg>
      <span>14 ALDER ROW<br>STE 210, MILLBROOK<br>CO 80512-1180</span>
    </div>
    <div class="contact-row">
      <svg width="13" height="13" viewBox="0 0 13 13"><path d="M3 0l2 3-1.5 1.5c.8 1.8 2.2 3.2 4 4L9 7l3 2-1 3C5 12 1 8 0 2z" fill="#fff"/></svg>
      <span>+1 555 0142 776</span>
    </div>
    <div class="contact-row">
      <svg width="14" height="11" viewBox="0 0 14 11"><rect width="14" height="11" fill="#fff"/><path d="M0 0l7 6 7-6" fill="none" stroke="#1d1d1f" stroke-width="1.2"/></svg>
      <span>hello@briskfern.com</span>
    </div>
  </address>
</section>

<footer class="section footer">
  <div class="footer-copy">Brisk Fern © 2016 All Rights Reserved.</div>
  <div class="footer-social"><span class="label">CONNECT WITH US</span><i></i><i></i><i></i><i></i></div>
</footer>

</body>
</html>
```